Salt Reef Squall - Ferrano Distillery

We need help designing a label for a Ready To Drink (RTD) canned beverage called "Salt Reef Squall".

We are a Distillery in Bunbury, Western Australia and you have done a canned beer label design work for a place called Tollick Brewery who we are working together with on the "Salt Reef Squall" (using their ginger beer). I have attached the Label you used for them titled Tollick Ginger Beer Can. You can use that for sizing at it will be the pretty much the same size just very marginally bigger.

We are called Ferrano Distillery as Ferrano is the latin word for Copper and all our stills are copper pot stills that we use to make the spirits. The can itself will likely be copper colour with a black lid.

We really have no real specific direction we want to go in so certainly leaving the artistic creativity to you guys. There's a few different concepts i would like to see created.

We have done a Rum label before (rum bottle attached) called Admiral Hemlock Pure Single Rum and we we were hoping to use somewhat similar style artwork on the can. However, instead of the words Pure, Single, Rum along the banner we were hoping to have "Salt Reef Squall" instead. Depending on pricing we may have the words on the badge metallic or slightly raised. My only concern with that is the Admiral Hemlock character would not be big enough so he would need to be redesigned to be larger and perhaps looking like he is coming out of the can or something. (hope that makes sense)

Another concept would be a doing a literal storm theme throughout. Like have a ship in rocky waters with lightning bolts and a more dark and broody theme to it or a washed up shipwreck during a storm.

As for the boring stuff... see how the Tollick ginger beer label is divided into somewhat three sections. We would like the blurb section to be slightly smaller area and the front/first section to be larger. I have attached the new barcode. I have also attached our QR code that we would want on there, the can will have the same mls - 375 however the ABV% will be 4.5% which means we need the standard drinks logo to change to 1.3. Pregnancy label kept the same and I will finalise the blurb once we have the flavour profile (in the coming days) however this will be a similar length. Remove the text at the bottom and the canning details may look neater in a small paragraph rather than down one side,

The middle section instead of a large Tollick logo it needs to be a smaller version without the "poured with purpose" part then "x" then our logo which is attached and underneath running across both logos text saying "Partnering for the Heart of the Salt Reef"

Kind regards,
Niall from Ferrano Distillery

Requirements
Must have
• Salt Reef Squall on the front of the can (this is name of the drink)

```html
<!DOCTYPE html>
<html lang="en">
<head>
<meta charset="utf-8">
<title>Salt Reef Squall – Tollick Brewery × Ferrano Distillery label</title>
<link rel="stylesheet" href="https://fonts.googleapis.com/css2?family=Cinzel:wght@500;700&family=Libre+Baskerville:wght@700&family=Oswald:wght@400&display=swap">
<style>
  :root {
    --page: #e9eaea;
    --label-black: #1c1c1c;
    --label-white: #f4f4f2;
    --trim-brown: #7a4a22;
    --band-brown: #6b4526;
    --gold: #e0a24a;
    --gold-soft: #f0b25a;
    --sky-top: #2f8fd0;
    --sky-mid: #8fcbe8;
    --figure-brown: #7d6346;
  }
  html, body {
    margin: 0;
    width: 1200px;
    height: 1200px;
    overflow: hidden;
    background: var(--page);
  }
  .canvas {
    width: 1200px;
    height: 1200px;
    display: flex;
    align-items: center;
    justify-content: center;
  }
  .label { width: 620px; height: 1100px; display: block; }
  .label-outline { fill: var(--label-black); stroke: var(--label-white); stroke-width: 7; }
  .label-trim { fill: none; stroke: var(--trim-brown); stroke-width: 1.4; }
  .brand-arch-top { font-family: "Cinzel", serif; font-weight: 700; font-size: 17px; fill: var(--label-white); letter-spacing: 0.5px; }
  .brand-arch-bottom { font-family: "Cinzel", serif; font-weight: 700; font-size: 17px; fill: var(--gold); letter-spacing: 0.5px; }
  .medallion-frame { fill: none; stroke: var(--trim-brown); stroke-width: 1.4; }
  .medallion-ring { fill: none; stroke: var(--gold); stroke-width: 7; }
  .title-main { font-family: "Libre Baskerville", serif; font-weight: 700; font-size: 34px; fill: var(--label-white); }
  .title-band { fill: var(--band-brown); }
  .title-sub { font-family: "Libre Baskerville", serif; font-weight: 700; font-size: 30px; fill: var(--gold-soft); }
  .title-dashes { stroke: var(--gold-soft); stroke-width: 1.6; }
  .tagline { font-family: "Oswald", sans-serif; font-size: 10px; fill: var(--gold); }
  .spec { font-family: "Libre Baskerville", serif; font-size: 8.5px; fill: var(--label-white); }
  .partner-name { font-family: "Cinzel", serif; font-weight: 700; font-size: 13px; fill: var(--label-white); }
  .divider { stroke: var(--trim-brown); stroke-width: 1; }
</style>
</head>
<body>
<main class="canvas">
  <svg class="label" viewBox="0 0 310 550" xmlns="http://www.w3.org/2000/svg">
    <defs>
      <linearGradient id="scene-fill" x1="0" y1="0" x2="0" y2="1">
        <stop offset="0" stop-color="var(--sky-top)"/>
        <stop offset="0.45" stop-color="var(--sky-mid)"/>
        <stop offset="0.6" stop-color="var(--figure-brown)"/>
        <stop offset="1" stop-color="#5a4632"/>
      </linearGradient>
      <path id="arch-top" d="M 72 72 Q 155 2 238 72"/>
      <path id="arch-bottom" d="M 66 486 Q 155 548 244 486"/>
    </defs>

    <path class="label-outline" d="M 60 60 Q 155 -52 250 60 L 290 60 Q 290 75 305 78 L 305 472 Q 290 475 290 490 L 250 490 Q 155 602 60 490 L 20 490 Q 20 475 5 472 L 5 78 Q 20 75 20 60 Z"/>
    <path class="label-trim" transform="translate(155 275) scale(0.94) translate(-155 -275)" d="M 60 60 Q 155 -52 250 60 L 290 60 Q 290 75 305 78 L 305 472 Q 290 475 290 490 L 250 490 Q 155 602 60 490 L 20 490 Q 20 475 5 472 L 5 78 Q 20 75 20 60 Z"/>

    <text class="brand-arch-top"><textPath href="#arch-top" startOffset="50%" text-anchor="middle">TOLLICK BREWERY</textPath></text>

    <path class="medallion-frame" d="M 32 318 L 32 185 Q 32 78 155 78 Q 278 78 278 185 L 278 318 Z"/>
    <circle cx="155" cy="200" r="110" fill="url(#scene-fill)" role="img" aria-label="Illustration: grinning skeleton in a checked shirt raising two beer bottles against a blue seaside sky"/>
    <circle class="medallion-ring" cx="155" cy="200" r="110"/>

    <text class="title-main" x="155" y="356" text-anchor="middle" textLength="262" lengthAdjust="spacingAndGlyphs">SALT REEF</text>
    <rect class="title-band" x="16" y="362" width="278" height="42"/>
    <g class="title-dashes">
      <line x1="30" y1="388" x2="33" y2="380"/><line x1="35" y1="388" x2="38" y2="380"/><line x1="40" y1="388" x2="43" y2="380"/><line x1="45" y1="388" x2="48" y2="380"/>
      <line x1="262" y1="388" x2="265" y2="380"/><line x1="267" y1="388" x2="270" y2="380"/><line x1="272" y1="388" x2="275" y2="380"/><line x1="277" y1="388" x2="280" y2="380"/>
    </g>
    <text class="title-sub" x="155" y="395" text-anchor="middle">SQUALL</text>

    <line class="divider" x1="20" y1="408" x2="290" y2="408"/>
    <text class="tagline" x="155" y="423" text-anchor="middle" textLength="230" lengthAdjust="spacingAndGlyphs">PARTNERING FOR THE HEART OF THE SALT REEF</text>
    <text class="spec" x="48" y="441">375 MLS</text>
    <text class="spec" x="262" y="441" text-anchor="end">ABV% 4.5%</text>
    <text class="partner-name" x="155" y="462" text-anchor="middle">Ferrano Distillery</text>

    <text class="brand-arch-bottom"><textPath href="#arch-bottom" startOffset="50%" text-anchor="middle">TOLLICK BREWERY</textPath></text>
  </svg>
</main>
</body>
</html>
```